Corsets, Cups and Commerce needs a book cover

I've been in lingerie business for 12 years, we own 5 x Lingerie stores. This is my story aimed at women in business or women who want to start a business. Essentially its a business book but also offers bra fitting advice. Although the book cover can be a bit cheeky it also needs to be tasteful. I do not have a colour in mind I just don't like it too girly. I like strong and bold with a feminine touch. The title needs to catch peoples attention when surrounded by so many other books. It needs to have some sort of image or texture. That could be a lace background texture. I like the idea of a bra hanging off the letters or some kind of image of a bra but a beautiful lacy bra. I would like the cover to be more beautiful than tacky even though it has the word 'boobs'.
Updates

Hi everyone, some great designs so far. Many of you have made a bra part of the 'Boobs' word. I thought this could work but it doesn't as it covers up the word 'Boobs' too much and I feel this word will catch peoples attention. If any of you would like to revise please feel free. thankyou Delphine.

Target Market(s)

Women in business or women wanting to start a business.

Industry/Entity Type

Retail

Logo Text

Corsets, Cups and Commerce

Font styles to use
Serif
Sans Serif

Colors

Designer to choose colors to be used in the design.

Requirements
Must have
• Title: Corsets, Cups and Commerce (you could replace 'and' with '&' if it works better.
• Tagline: Steady Lessons for Women in Trade
• Author: Delphine Karsby
Nice to have
• An image of a bra, maybe in a playful way. It could hang off the letters or maybe the letters could look like a bra, but I'm concerned it may look tacky that way. Somehow incorporate a picture of a bra preferably as part of the title.
• I don't have images for you, you have the freedom to choose.
Should not have
• Although this book has boobs and bras in the title it must not be tacky or sexual. It is a business book.
• I do not like it to look too girly, probably not script unless its subtle.

```html
<!DOCTYPE html>
<html lang="en">
<head>
<meta charset="utf-8">
<title>Corsets, Cups and Commerce — Book Cover</title>
<link rel="stylesheet" href="https://fonts.googleapis.com/css2?family=Montserrat:wght@400;600&display=swap">
<style>
  :root {
    --paper: #ffffff;
    --ink: #0d0c10;
    --frame: #1a1a1a;
    --lace-light: #ece9e3;
    --lace-mid: #cfcac1;
    --lace-deep: #b7b0a4;
    --plum: #5b2a5e;
    --plum-deep: #4a1f4d;
  }
  html, body {
    margin: 0;
    padding: 0;
    width: 840px;
    height: 1200px;
    overflow: hidden;
    background: var(--paper);
  }
  .cover {
    position: relative;
    width: 840px;
    height: 1200px;
    box-sizing: border-box;
    border: 1.5px solid var(--frame);
    background: var(--paper);
    font-family: 'Montserrat', sans-serif;
  }
  .cover-art {
    position: absolute;
    inset: 0;
    width: 840px;
    height: 1200px;
  }
  .title-line {
    font-family: 'Montserrat', sans-serif;
    font-weight: 600;
    font-size: 196px;
    fill: var(--ink);
  }
  .title-line--lace {
    fill: url(#laceTone);
    filter: url(#softShadow);
  }
  .tagline {
    font-family: 'Montserrat', sans-serif;
    font-weight: 400;
    font-size: 41px;
    fill: var(--ink);
  }
  .author {
    font-family: 'Montserrat', sans-serif;
    font-weight: 400;
    font-size: 88px;
    fill: var(--ink);
  }
</style>
</head>
<body>
<main class="cover">
  <svg class="cover-art" viewBox="0 0 840 1200" xmlns="http://www.w3.org/2000/svg">
    <defs>
      <linearGradient id="laceTone" x1="0" y1="0" x2="1" y2="1">
        <stop offset="0" stop-color="var(--lace-mid)"/>
        <stop offset="0.5" stop-color="var(--lace-light)"/>
        <stop offset="1" stop-color="var(--lace-deep)"/>
      </linearGradient>
      <linearGradient id="plumTone" x1="0" y1="0" x2="0" y2="1">
        <stop offset="0" stop-color="var(--plum)"/>
        <stop offset="1" stop-color="var(--plum-deep)"/>
      </linearGradient>
      <filter id="softShadow" x="-10%" y="-10%" width="120%" height="130%">
        <feDropShadow dx="0" dy="6" stdDeviation="6" flood-color="#000" flood-opacity="0.18"/>
      </filter>
    </defs>

    <g class="title">
      <text class="title-line" x="144" y="216" textLength="566" lengthAdjust="spacingAndGlyphs">CORSETS,</text>
      <text class="title-line title-line--lace" x="102" y="390" textLength="500" lengthAdjust="spacingAndGlyphs">CUPS</text>
      <text class="title-line" x="636" y="390" textLength="114" lengthAdjust="spacingAndGlyphs">&amp;</text>
      <text class="title-line" x="76" y="538" textLength="684" lengthAdjust="spacingAndGlyphs">COMMERCE</text>
    </g>

    <g class="tagline-block">
      <text class="tagline" x="426" y="650" text-anchor="middle">Steady Lessons</text>
      <text class="tagline" x="426" y="710" text-anchor="middle">for Women in</text>
      <text class="tagline" x="426" y="772" text-anchor="middle">Trade</text>
    </g>

    <rect class="bra-artwork" x="120" y="796" width="616" height="188" rx="90"
          fill="url(#plumTone)" role="img" aria-label="Illustration of a plum-coloured textured bra"/>

    <text class="author" x="76" y="1116" textLength="704" lengthAdjust="spacingAndGlyphs">Delphine Karsby</text>
  </svg>
</main>
</body>
</html>
```